Business Card

We would like a very clean corporate, two sided business card that conveys that we are a quality focused, reliable organisation that can make a business better. We focus on a cycle of continuous improvement for IT systems.

The brief is primarily clean and corporate, nothing overly complicated.

We sell IT services, IT support, server implementation, problem solving services to businesses in Australia.

Business

```html
<!DOCTYPE html>
<html lang="en">
<head>
<meta charset="utf-8">
<title>Veritec Loop – Business Card</title>
<link rel="stylesheet" href="https://fonts.googleapis.com/css2?family=Source+Sans+3:wght@400;600;700&display=swap">
<style>
  :root {
    --navy: #262a3f;
    --pink: #e8175d;
    --white: #ffffff;
    --grey-light: #f4f4f5;
    --grey-mid: #e3e3e5;
    --text: #2b2b33;
    --rule: #4a4a55;
    --backdrop: #efeceb;
  }
  * { margin: 0; padding: 0; box-sizing: border-box; }
  html, body { width: 1200px; height: 900px; overflow: hidden; }
  body {
    background: var(--backdrop);
    font-family: "Source Sans 3", sans-serif;
    color: var(--text);
    position: relative;
  }
  .card {
    position: absolute;
    top: 298px;
    width: 504px;
    height: 288px;
    border-radius: 18px;
    overflow: hidden;
    background: linear-gradient(180deg, var(--white) 0%, var(--grey-light) 35%, var(--grey-mid) 70%);
    box-shadow: 0 2px 6px rgba(0,0,0,0.15);
  }
  .card--front { left: 75px; }
  .card--back { left: 622px; }
  .card__wave { position: absolute; left: 0; top: 0; width: 504px; height: 288px; }

  .wordmark {
    position: absolute;
    font-weight: 600;
    color: var(--navy);
    letter-spacing: 0.5px;
    line-height: 1;
    display: flex;
    align-items: center;
    gap: 12px;
  }
  .wordmark__dot { width: 14px; height: 14px; background: var(--pink); border-radius: 50%; }
  .card--front .wordmark { left: 140px; top: 48px; font-size: 42px; }
  .card--back .wordmark { left: 20px; top: 102px; font-size: 36px; }

  .web {
    position: absolute;
    left: 300px; top: 118px;
    font-size: 12.5px;
    letter-spacing: 2px;
    color: var(--navy);
  }

  .holder { position: absolute; left: 22px; top: 178px; }
  .holder__name { font-size: 15px; font-weight: 700; color: var(--navy); }
  .holder__role { font-size: 11px; margin-top: 1px; }

  .contact {
    position: absolute;
    left: 22px; top: 230px;
    display: flex;
    font-size: 9.5px;
    line-height: 13.5px;
  }
  .contact__block { padding-right: 11px; }
  .contact__block + .contact__block { border-left: 1px solid var(--rule); padding-left: 11px; }
  .contact__company { font-weight: 700; }
</style>
</head>
<body>

<section class="card card--front" aria-label="Card front">
  <svg class="card__wave" viewBox="0 0 504 288" aria-hidden="true">
    <path d="M0 115 C110 112 190 162 300 170 C380 176 450 160 504 145 L504 288 L0 288 Z" fill="var(--pink)"/>
    <path d="M0 142 C110 142 200 172 300 177 C390 181 450 170 504 162 L504 288 L0 288 Z" fill="var(--navy)"/>
    <path d="M0 160 C110 162 200 185 300 187 C390 188 450 178 504 174 L504 288 L0 288 Z" fill="var(--white)"/>
  </svg>
  <div class="wordmark">veritec loop <span class="wordmark__dot"></span></div>

  <div class="holder">
    <p class="holder__name">Dana Whitford</p>
    <p class="holder__role">President</p>
  </div>

  <div class="contact">
    <div class="contact__block">
      <p class="contact__company">Veritec Loop Pty Ltd</p>
      <p>Suite 214, 40-44 Miller Lane</p>
      <p>Harbourview, NSW, 2100 Australia</p>
    </div>
    <div class="contact__block">
      <p>PH: +61 2 5550 1184</p>
      <p>FAX: +61 2 5550 1197</p>
    </div>
    <div class="contact__block">
      <p>MAIL : dana@veritecloop.net</p>
      <p>ABN: 00 123 456 789</p>
    </div>
  </div>
</section>

<section class="card card--back" aria-label="Card back">
  <svg class="card__wave" viewBox="0 0 504 288" aria-hidden="true">
    <path d="M0 207 C110 205 190 255 300 262 C380 266 450 250 504 236 L504 288 L0 288 Z" fill="var(--pink)"/>
    <path d="M0 238 C110 238 200 266 300 270 C390 272 450 264 504 256 L504 288 L0 288 Z" fill="var(--navy)"/>
    <path d="M0 255 C110 257 200 276 300 278 C390 279 450 272 504 268 L504 288 L0 288 Z" fill="var(--white)"/>
  </svg>
  <div class="wordmark">veritec loop <span class="wordmark__dot"></span></div>
  <p class="web">www.veritecloop.net</p>
</section>

</body>
</html>
```